Pellbry Redesign of Website

I require my webpage to look different but this is out with my current providers platform
Updates
I will benefit from designs that use my wording (this is extremely important). I appreciate there may be a lot of wording in some areas so i would be happy with "read more" in various places. The use of my face in photo is a must and my logo is also a must which can be found on m y website www.pellbryfocus.co.uk I do not want corporate feel, i would like a warm, authentic. personal and inviting feel.
5+ page

```html
<!DOCTYPE html>
<html lang="en">
<head>
<meta charset="utf-8">
<title>The Story Behind Pellbry</title>
<link href="https://fonts.googleapis.com/css2?family=Noto+Serif:wght@400;500&family=Outfit:wght@300;400;500&family=Dancing+Script:wght@500&display=swap" rel="stylesheet">
<style>
:root{
  --bg:#f1f1f1;
  --sidebar:#ffffff;
  --ink:#1f2b2a;
  --muted:#5f6664;
  --teal:#17a58a;
  --teal-dark:#0f8c74;
  --gold:#f7d68c;
  --forest:#1d4a3f;
  --card:#f6f6f6;
  --white:#ffffff;
}
*{box-sizing:border-box;margin:0;padding:0}
html,body{width:1200px;height:2496px;overflow:hidden}
body{background:var(--bg);font-family:"Outfit",sans-serif;color:var(--ink);position:relative}

/* sidebar */
.sidebar{position:absolute;left:0;top:0;width:247px;height:2496px;background:var(--sidebar)}
.brand{position:absolute;left:0;width:247px;top:18px;text-align:center}
.brand-mark{width:78px;height:78px;border-radius:50%;background:#f3e6d6;margin:0 auto 6px}
.brand-name{font-family:"Noto Serif",serif;font-size:20px;letter-spacing:1.5px;color:var(--ink)}
.nav{position:absolute;left:40px;top:186px;list-style:none}
.nav li{height:68px;display:flex;align-items:center;gap:20px;font-size:15px;color:var(--ink)}
.nav li.active{color:var(--teal)}
.nav svg{width:32px;height:32px;fill:none;stroke:var(--ink);stroke-width:1.3;stroke-linecap:round;stroke-linejoin:round}
.nav li.active svg{stroke:var(--teal)}

/* main */
.abs{position:absolute}
.tagline{left:283px;top:88px;font-family:"Dancing Script",cursive;color:var(--teal);font-size:24px}
.title{left:283px;top:126px;font-family:"Noto Serif",serif;font-size:50px;line-height:60px;font-weight:400}
.intro-name{left:283px;top:255px;display:flex;align-items:center;gap:20px;font-size:14px;font-weight:500}
.intro-name::before{content:"";width:50px;height:1px;background:var(--ink)}
.intro{left:283px;top:294px}
.intro p{font-size:12.6px;line-height:17px;color:#2f3634;font-weight:300;width:490px}
.intro p+p{margin-top:17px}
.quote{left:283px;top:412px;width:483px;height:70px;background:var(--white);border-radius:6px;box-shadow:0 4px 14px rgba(0,0,0,.05);display:flex;align-items:center;padding-left:18px;gap:16px}
.quote p{font-size:12.6px;line-height:17px;font-weight:300;position:relative}
.quote p::before{content:"\201C";position:absolute;left:-14px;top:-8px;color:var(--teal);font-family:"Noto Serif",serif;font-size:18px}
.quote b{color:var(--teal);font-family:"Noto Serif",serif;font-size:18px}
.portrait-back{left:864px;top:90px;width:251px;height:318px;background:#bdbdbd}
.portrait{left:855px;top:79px;width:251px;height:320px;background:linear-gradient(160deg,#e6e3df,#cfc8c1 55%,#1e4e52 85%);border:4px solid #eaeaea}

.h2{font-family:"Noto Serif",serif;font-size:31px;font-weight:400}

/* journey */
.step{left:283px;width:833px;height:128px}
.ring{position:absolute;left:0;top:0;width:128px;height:128px;border-radius:50%}
.ring.teal{background:conic-gradient(from 180deg,var(--teal) 0 50%,transparent 50%)}
.ring.gold{background:conic-gradient(from 180deg,var(--gold) 0 50%,transparent 50%)}
.ring .disc{position:absolute;left:11px;top:11px;width:106px;height:106px;border-radius:50%;background:var(--white);box-shadow:2px 4px 10px rgba(0,0,0,.1);display:flex;align-items:center;justify-content:center}
.disc svg{width:54px;height:54px;fill:none;stroke:var(--ink);stroke-width:1.6;stroke-linecap:round;stroke-linejoin:round}
.step .card{position:absolute;left:144px;top:4px;width:689px;height:121px;background:var(--card);border-radius:4px;box-shadow:0 2px 8px rgba(0,0,0,.04);padding:0 70px 0 29px;display:flex;flex-direction:column;justify-content:center}
.card h3{font-family:"Noto Serif",serif;font-size:13.6px;font-weight:400;line-height:17px;margin-bottom:8px}
.card p{font-size:12.5px;line-height:17px;color:var(--muted);font-weight:300}

/* why grid */
.photo{position:absolute;width:194px}
.tile{position:absolute;width:194px;background:var(--white);border-radius:4px;padding:14px 11px;box-shadow:0 3px 10px rgba(0,0,0,.04)}
.tile h3{font-family:"Noto Serif",serif;font-size:14px;line-height:17px;font-weight:400;margin-bottom:10px}
.tile p{font-size:12.6px;line-height:17px;color:var(--muted);font-weight:300}

/* path */
.milestone{position:absolute;width:200px}
.milestone .icon{width:74px;height:74px;border-radius:50%;background:var(--white);box-shadow:0 3px 8px rgba(0,0,0,.08);display:flex;align-items:center;justify-content:center}
.milestone svg{width:40px;height:40px;fill:none;stroke:var(--teal-dark);stroke-width:1.5;stroke-linecap:round;stroke-linejoin:round}
.milestone span{display:block;margin-top:16px;font-size:13.5px;line-height:17px;color:#2f3634;font-weight:300}

/* banner */
.banner{left:283px;top:2346px;width:833px;height:114px;background:var(--forest);border-radius:32px;color:#fff;display:flex;align-items:center}
.banner .heart{width:72px;height:72px;border-radius:50%;border:1.5px solid #e8d8b0;margin-left:124px;display:flex;align-items:center;justify-content:center;flex:none}
.banner .heart svg{width:36px;height:36px;fill:none;stroke:#f0e0b8;stroke-width:2}
.banner .text{margin-left:20px}
.banner h2{font-family:"Noto Serif",serif;font-weight:400;font-size:19px;line-height:21px}
.banner p{font-size:9.5px;line-height:13px;margin-top:7px;font-weight:300;width:380px}
</style>
</head>
<body>

<aside class="sidebar">
  <div class="brand">
    <div class="brand-mark"></div>
    <div class="brand-name">PELLBRY</div>
  </div>
  <ul class="nav">
    <li class="active"><svg viewBox="0 0 32 32"><path d="M5 15 16 5l11 10M8 13v14h16V13M13 27v-7h6v7"/></svg>Home</li>
    <li><svg viewBox="0 0 32 32"><circle cx="16" cy="16" r="11"/><path d="M16 5v22M10 11c3 1 3 4 0 5M22 11c-3 1-3 4 0 5"/></svg>My Journey</li>
    <li><svg viewBox="0 0 32 32"><circle cx="16" cy="16" r="11"/><path d="M11 20l4-8 3 6 3-4"/></svg>Coaching &amp; Support</li>
    <li><svg viewBox="0 0 32 32"><path d="M4 24h6l6 2 10-5-2-2-8 2M10 19h6M19 10c0-2 3-3 4 0 1-3 4-2 4 0 0 3-4 5-4 5s-4-2-4-5z"/></svg>How We Can Help</li>
    <li><svg viewBox="0 0 32 32"><circle cx="14" cy="11" r="5"/><path d="M5 27c0-6 4-9 9-9s9 3 9 9z"/></svg>Work With Me</li>
    <li><svg viewBox="0 0 32 32"><path d="M4 10l12 4 12-4v14l-12 4-12-4zM16 14v14"/></svg>Resources</li>
    <li><svg viewBox="0 0 32 32"><circle cx="16" cy="16" r="12"/><circle cx="16" cy="13" r="4"/><path d="M9 24c2-4 12-4 14 0"/></svg>About Pellbry</li>
    <li><svg viewBox="0 0 32 32"><path d="M5 8h14v10H11l-4 3v-3H5zM22 12h5v9h-2v3l-3-3h-6v-3"/></svg>Contact</li>
  </ul>
</aside>

<main>
  <section class="hero">
    <p class="abs tagline">Helping others began with understanding myself.</p>
    <h1 class="abs title">The Story<br>Behind Pellbry</h1>
    <p class="abs intro-name">My name is Elspeth Marr Doyle, founder of Pellbry.</p>
    <div class="abs intro">
      <p>I am an ADHD coach and wellbeing practitioner with lived experience of ADHD and autism (AuDHD).</p>
      <p>I combine professional expertise with real-life experience to offer compassionate, practical support that helps you better understand yourself, your brain, and your wellbeing.</p>
    </div>
    <div class="abs quote">
      <svg width="34" height="30" viewBox="0 0 34 30"><path d="M17 28S2 19 2 10a7.5 7.5 0 0 1 15-2 7.5 7.5 0 0 1 15 2c0 9-15 18-15 18z" fill="#2ab597" stroke="#1f2b2a" stroke-width="1.3"/></svg>
      <p>You don't need to have everything figured out before reaching out.<br>We'll take things one step at a time, together. <b>&#8221;</b></p>
    </div>
    <div class="abs portrait-back"></div>
    <div class="abs portrait" role="img" aria-label="Portrait photograph of the founder"></div>
  </section>

  <section class="journey">
    <h2 class="abs h2" style="left:283px;top:548px">My Journey</h2>

    <div class="abs step" style="top:620px">
      <div class="ring teal"><div class="disc"><svg viewBox="0 0 54 54"><path d="M18 44v-8c-5-3-7-8-6-14 2-9 11-13 19-11 7 2 11 8 10 15l3 6-3 1v5c0 2-2 3-4 3h-4v3"/><path d="M24 20c2-3 7-3 8 1M22 27c3 1 6 0 7-2"/></svg></div></div>
      <div class="card"><h3>My adult ADHD diagnosis came during a period of profound self-discovery following a mental health breakdown.</h3><p>For many years, my ADHD went unrecognised and was treated only with antidepressants, which never addressed the underlying cause of my struggles. Learning about ADHD didn't cause my breakdown — it helped explain it.</p></div>
    </div>

    <div class="abs step" style="top:767px">
      <div class="ring gold"><div class="disc"><svg viewBox="0 0 54 54"><path d="M27 27c-5-8-14-9-15-2-1 9 10 8 15 2zm0 0c5-8 14-9 15-2 1 9-10 8-15 2z"/></svg></div></div>
      <div class="card"><h3>As my understanding grew, I recognised I am also autistic — something that is common alongside ADHD.</h3><p>Around 50–70% of autistic people also have ADHD, and many adults only recognise the second neurotype once the first has been identified. This combined experience is often called AuDHD. For me, it brought even greater clarity.</p></div>
    </div>

    <div class="abs step" style="top:913px">
      <div class="ring teal"><div class="disc"><svg viewBox="0 0 54 54"><path d="M27 38s-10-6-10-13a5 5 0 0 1 10-2 5 5 0 0 1 10 2c0 7-10 13-10 13zM27 8v4M27 43v4M10 25h4M40 25h4M14 13l3 3M40 13l-3 3M14 37l3-3M40 37l-3-3"/></svg></div></div>
      <div class="card"><h3>These experiences strengthened my passion for helping neurodivergent individuals better understand their brains, develop self-compassion and find strategies that work.</h3><p>I believe every brain deserves understanding, support and practical tools for wellbeing.</p></div>
    </div>

    <div class="abs step" style="top:1060px">
      <div class="ring gold"><div class="disc"><svg viewBox="0 0 54 54"><path d="M6 20l21-9 21 9-21 9zM15 24v10c6 5 18 5 24 0V24M44 22v11"/><circle cx="44" cy="35" r="1.6"/></svg></div></div>
      <div class="card"><h3>This personal journey inspired me to deepen my professional knowledge and training.</h3><p>I qualified as an Integrative Counsellor (HNC) and then as a Health &amp; Wellbeing Coach through Clearwater Pathways Academy (HWC-recognised), followed by specialist training in Autism, ADHD and Somatic Coaching.</p></div>
    </div>
  </section>

  <section class="why">
    <h2 class="abs h2" style="left:283px;top:1256px">Why Pellbry Was Created</h2>

    <div class="photo" style="left:283px;top:1323px;height:315px;background:linear-gradient(180deg,#b9c9d6,#6f8a55 45%,#5e8a2a 75%,#8fb135)" role="img" aria-label="Sunlit green hills and tea fields"></div>
    <div class="tile" style="left:283px;top:1654px;height:176px"><h3>I wanted to offer the kind of support I wish I had when I was struggling.</h3><p>A safe, welcoming space where neurodivergent people feel seen, understood and supported to thrive in their own way.</p></div>

    <div class="tile" style="left:496px;top:1345px;height:178px"><h3>I believe in practical, lasting support.</h3><p>I empower people with knowledge, strategies and tools they can continue using long after our work together has ended.</p></div>
    <div class="photo" style="left:496px;top:1538px;height:314px;background:linear-gradient(180deg,#d9d6cf,#b35a4e 50%,#5a4a42)" role="img" aria-label="Group support session in a bright room"></div>

    <div class="photo" style="left:709px;top:1323px;height:315px;background:linear-gradient(180deg,#d9a95a,#8a7d6a 45%,#3e4a5c)" role="img" aria-label="Happy family outdoors in autumn"></div>
    <div class="tile" style="left:709px;top:1654px;height:176px"><h3>I understand the reality of neurodivergent family life.</h3><p>As a mother to three neurodivergent children, I have invaluable lived experience of advocacy, navigating systems and creating a calmer home life.</p></div>

    <div class="tile" style="left:922px;top:1345px;height:178px"><h3>My personal experiences and professional qualifications shape the compassionate, neuro-affirming approach at the heart of everything I do.</h3></div>
    <div class="photo" style="left:922px;top:1538px;height:314px;background:linear-gradient(180deg,#4fa8c8,#6fb9d4 40%,#e08a3a 75%,#c9732c)" role="img" aria-label="Speaker presenting on stage"></div>
  </section>

  <section class="path">
    <h2 class="abs h2" style="left:284px;top:1946px">My Path</h2>

    <div class="milestone" style="left:283px;top:2052px"><div class="icon"><svg viewBox="0 0 40 40"><path d="M5 20 20 7l15 13M9 17v18h22V17M17 35v-9h6v9"/></svg></div><span>Housing Officer</span></div>
    <div class="milestone" style="left:503px;top:2052px"><div class="icon"><svg viewBox="0 0 40 40"><path d="M14 34v-6c-4-2-5-6-4-10 1-7 8-10 14-8 5 1 8 6 7 11l2 4-2 1v3c0 2-1 2-3 2h-3v3"/></svg></div><span>Mental Health Breakdown</span></div>
    <div class="milestone" style="left:724px;top:2052px"><div class="icon"><svg viewBox="0 0 40 40"><circle cx="20" cy="18" r="10"/><path d="M20 8v20M14 14c3 1 3 4 0 5M26 14c-3 1-3 4 0 5M12 34h16"/></svg></div><span>ADHD Diagnosis</span></div>
    <div class="milestone" style="left:945px;top:2052px"><div class="icon"><svg viewBox="0 0 40 40"><path d="M20 20c-4-6-11-7-12-2-1 7 8 6 12 2zm0 0c4-6 11-7 12-2 1 7-8 6-12 2z"/></svg></div><span>Understanding Autism<br>(AuDHD)</span></div>

    <div class="milestone" style="left:283px;top:2188px"><div class="icon"><svg viewBox="0 0 40 40"><path d="M6 24l16-9 12 6-16 9zM6 24v5l12 6 16-9v-5M18 30v5"/></svg></div><span>Integrative Counselling<br>Study</span></div>
    <div class="milestone" style="left:503px;top:2188px"><div class="icon"><svg viewBox="0 0 40 40"><path d="M4 16l16-7 16 7-16 7zM11 19v8c4 4 14 4 18 0v-8M33 17v9"/></svg></div><span>Health &amp; Wellbeing Coach<br>(HWC-recognised)</span></div>
    <div class="milestone" style="left:724px;top:2188px"><div class="icon"><svg viewBox="0 0 40 40"><path d="M14 34v-6c-4-2-5-6-4-10 1-7 8-10 14-8 5 1 8 6 7 11l2 4-2 1v3c0 2-1 2-3 2h-3v3M20 22s-4-2-4-5a2 2 0 0 1 4-1 2 2 0 0 1 4 1c0 3-4 5-4 5z"/></svg></div><span>Specialist Training in Autism,<br>ADHD &amp; Somatic Coaching</span></div>
    <div class="milestone" style="left:945px;top:2188px"><div class="icon"><svg viewBox="0 0 40 40"><path d="M4 32l10-18 8 12 5-7 9 13zM18 20l2 2 2-2"/></svg></div><span>Pellbry Created</span></div>
  </section>

  <section class="abs banner">
    <div class="heart"><svg viewBox="0 0 36 36"><path d="M18 31S4 23 4 13a7 7 0 0 1 14-3 7 7 0 0 1 14 3c0 10-14 18-14 18z"/></svg></div>
    <div class="text">
      <h2>Because sometimes the smallest changes<br>can make the biggest difference.</h2>
      <p>Whether you are looking to better understand yourself, develop new strategies, receive practical support or simply have someone who understands, I'm here for you.</p>
    </div>
  </section>
</main>

</body>
</html>
```